card design for engineering consultancy

engineering drafting and project management company the provides drafting services for.
Electrical, Hydraulic, Mechanical, and Civil services
The company is called Q7R Services and logo is as attached
Information on card should be.
1. Logo
2.website : Q7RServices.example
3. email : info@Q7RServices.example
4. Phone: (+61) 400512836
5. Motto: Design - Document - Develop - Deliver

this card should be basically used for business identification only

Target Market(s)

electricians plumbers air conditioning installers and civil contractors

Industry/Entity Type

engineering, drafting, electrical, plumbing, airconditioning, civil

Contact Information for Business Card

1. Logo 2.website : Q7RServices.example 3. email : info@Q7RServices.example 4. Phone: (+61) 400512836 5. Motto: Design - Document - Develop - Deliver

Font styles to use
Serif

Requirements
Must have
• logo
Nice to have
• something inovative and different that makes it stand out from being just another business card

```html
<!DOCTYPE html>
<html lang="en">
<head>
<meta charset="utf-8">
<title>Q7R Services – Business Card</title>
<link rel="stylesheet" href="https://fonts.googleapis.com/css2?family=Roboto:wght@400;700&display=swap">
<style>
  :root {
    --brand-red: #ec1c24;
    --brand-charcoal: #4a4a4c;
    --pattern-light: #777779;
    --pattern-dark: #4f4f51;
    --card-white: #ffffff;
    --backdrop: #ececec;
    --text-font: "Roboto", Arial, sans-serif;
  }
  * { box-sizing: border-box; margin: 0; padding: 0; }
  html, body { width: 1200px; height: 1000px; overflow: hidden; }
  body { background: var(--backdrop); font-family: var(--text-font); position: relative; }

  .card { position: absolute; border-radius: 40px; overflow: hidden; }

  /* Front */
  .card-front { left: 122px; top: 102px; width: 736px; height: 408px; background: var(--card-white); }
  .edge { position: absolute; width: 46px; }
  .edge-left-top { left: 0; top: 0; height: 238px; background: var(--brand-red); }
  .edge-left-bottom { left: 0; top: 238px; bottom: 0; background: var(--brand-charcoal); }
  .edge-right-top { right: 0; top: 0; height: 173px; background: var(--brand-charcoal); }
  .edge-right-bottom { right: 0; top: 173px; bottom: 0; background: var(--brand-red); }

  .front-name {
    position: absolute; left: 84px; top: 180px;
    font-weight: 700; font-size: 38px; letter-spacing: 1px;
    color: var(--brand-charcoal);
  }
  .contact-divider { position: absolute; left: 371px; top: 148px; width: 3px; height: 114px; background: var(--brand-charcoal); }
  .divider-accent { position: absolute; left: 0; bottom: 0; width: 3px; height: 50px; background: var(--brand-red); }
  .contact-list { position: absolute; left: 386px; top: 144px; list-style: none; }
  .contact-item { display: flex; align-items: center; height: 24px; margin-bottom: 24px; font-size: 18px; }
  .contact-item svg { width: 16px; height: 16px; margin-right: 16px; flex: none; }
  .contact-phone, .contact-web { color: var(--brand-red); }
  .contact-email { color: var(--brand-charcoal); }

  /* Back */
  .card-back {
    left: 288px; top: 532px; width: 730px; height: 410px;
    background: radial-gradient(circle at 50% 52%, var(--pattern-light) 0 22%, var(--pattern-dark) 60%, var(--pattern-light) 100%);
  }
  .pattern-field { position: absolute; inset: 0; }
  .side-tab {
    position: absolute; top: 86px; width: 42px; height: 248px;
    background: var(--brand-red); border: 5px solid var(--card-white);
  }
  .side-tab-left { left: -5px; border-radius: 0 40px 40px 0; }
  .side-tab-right { right: -5px; border-radius: 40px 0 0 40px; }
  .back-name {
    position: absolute; left: 0; right: 0; top: 190px; text-align: center;
    font-weight: 700; font-size: 44px; letter-spacing: 1px; color: var(--card-white);
  }
  .motto {
    position: absolute; left: 0; right: 0; top: 302px; text-align: center;
    font-weight: 700; font-size: 18px; color: var(--card-white);
  }
</style>
</head>
<body>
  <section class="card card-front" aria-label="Card front">
    <div class="edge edge-left-top"></div>
    <div class="edge edge-left-bottom"></div>
    <div class="edge edge-right-top"></div>
    <div class="edge edge-right-bottom"></div>

    <div class="front-name">Q7R Services</div>

    <div class="contact-divider"><span class="divider-accent"></span></div>
    <ul class="contact-list">
      <li class="contact-item contact-phone">
        <svg viewBox="0 0 16 16" aria-hidden="true"><path fill="currentColor" d="M3.6 1.2l2.2 2.6-1.3 1.7c.9 2 2.4 3.6 4.4 4.5l1.7-1.3 2.6 2.2-1.3 2.3C7 12.9 3.1 9 2.2 3z"/></svg>
        (+61) 400512836
      </li>
      <li class="contact-item contact-email">
        <svg viewBox="0 0 16 16" aria-hidden="true"><rect x="1" y="4" width="14" height="9" fill="currentColor"/><path d="M1.5 4.5L8 9.5l6.5-5" stroke="#fff" stroke-width="1.3" fill="none"/></svg>
        info@Q7RServices.example
      </li>
      <li class="contact-item contact-web">
        <svg viewBox="0 0 16 16" aria-hidden="true"><path fill="currentColor" d="M4 1l9 8.2-4 .4 2.4 4.6-1.8.9-2.3-4.7L4 13z"/></svg>
        www.Q7RServices.example
      </li>
    </ul>
  </section>

  <section class="card card-back" aria-label="Card back">
    <div class="pattern-field" role="img" aria-label="Grey concentric rounded-stripe background pattern"></div>
    <div class="side-tab side-tab-left"></div>
    <div class="side-tab side-tab-right"></div>
    <div class="back-name">Q7R Services</div>
    <p class="motto">Design || Document || Develop || Deliver</p>
  </section>
</body>
</html>
```